Nutritional & Gastrointestinal Health Consulting Service-Website design

We need a website design for a new health consulting service called "Bright Harbor" based in Perth, Australia.

We will be providing consulting services in the areas of:
1) Nutrition and Diet
2) Gastrointestinal Health (which means stomach & digestive system related health)

These consulting services will be provided by an Accredited Dietitian and a Paediatric Gastroenterologist.

We are open to creative ideas in terms of design, layout, fonts and colours. We also would love to see images of nature in the backdrop with families (adults with kids) having a good time, fresh fruits and vegetables displayed in a farmer's market or supermarket. 2 or 3 images should be sufficient. We would also definitely want our logo somewhere in the main page of website. The logo file is also attached. Please have a look at a website's design that we really liked. We would love to see designs inspired by that style. The website details are in the in the "nice to have priorities" section of this project brief.

We also would be looking at website designers with software coding skills so that if we like the design we can go ahead with the next step of coding.

The website design should communicate the purpose of the website and at the same time be simple, elegant and unique/eye-catching.

We look forward to receiving creative ideas for our website from you all. Good luck!
Updates

More details have been added to our project- for example: Logo, fonts style, must haves etc etc. Please view the updated project brief. Looking forward to receiving your fantastic ideas for our website. Thanking you

Hi, I have updated the colour preference. Will add the content preferences tomorrow. thanks

Hello all, I have now added a LOT more content to what we want in our website. It is very much in detail, so please carefully have a read through the entire project brief. If you have any questions write back to me and I will try to respond as quickly as I can. Last few days were busy so couldn't respond quickly to all of you who had send me designs/queries/questions. Thank you for your patience. I look forward to receiving fantastic designs from you all. Good Luck :-)

Target Market(s)

Adults based in western speaking countries aged 18 to 60 years

Industry/Entity Type

Software

Font styles to use
Sans Serif
Script

Colors
faa54b
acd036

Requirements
Must have
• The website must have the MAIN logo file attached. I have attached 3 files: 1) MAIN logo; 2) supplementary logo A ; 3) supplementary logo B

I have selected 2 colours from the colour scheme (see below)-(as the colour of our logo is that).
However we would also like to see LIGHT CHOCOLATE BROWN or CHOCOLATE BROWN colour used as the background colour of the website
Preferred WEBSITE CONTENT:
1) HOME PAGE:
Content required=
--Company Logo
--Dr Ravel Ostrin
Paediatric Gastroenterologist & Hepatologist
-Leora Ostrin.
Dietitian & Nutritionist
--Website Menu (either listed horizontally or vertically):
Once clicked on each name:

Under each of the Website Menu items we want the following Headings to be added

2) ABOUT US page:
Sub-heading under this: Qualification, Skills, Special Interest

3) SERVICES
RAVEL'S PAGE: Individual Consultation, Endoscopy procedures
Individual Consultation, Group Based Services, Food Diary, Food & Symptom Diary

4) FEES & REBATE: Content as below:
Please Note: Payment of full fees is required at the time of consultation and procedures. 48 hours notice is required for cancellation of appointments/non-attendance. Failure to provide this may result in a fee being incurred. Please call reception to find out the amount of fee charged for cancellation of appointments/non-attendance.
headings are:
Paediatric Gastroenterology:
Ravel's pge
Individual Consultation - Initial (upto 30 mins):
Review Consultation (upto 15 mins):
Endoscopy procedures - No Gap fees charged. Fees will be billed directly to Carewell. If any queries, please contact reception.

leora's pge
sub heading:
Individual Consultation - Initial (upto 45 mins):
Individual Consultation - Review (upto 30 mins):

Concession-Individual Consultation -Initial (upto 45 mins):
Concession-Individual Consultation - Review (upto 30 mins):
Please Note: Concession applies for health care card holders & pensioners

Group Based Services: Pricing subject to the type of service provided. Please contact us for an obligation free quote.
Education Topics Include:
- Paediatric Nutrition (Introducing Solids, Fussy Eating, Healthy Eating)
- Pregnancy Nutrition, Gestational Diabetes, Breastfeeding/Lactation Nutrition
- Healthy Eating, Supermarket Shopping Tips, Nutrition Label Reading Tips, Healthier
sub heading under nutrition & diet:
-Carewell:
--A rebate of $52.95 is available from Carewell if an EPC ( Enhanced Primary Care)/Chronic Disease Management (CDM) plan is issued by your GP.
--All mandatory paperwork needs to be available at the time of making your appointment for your eligibility.
-Private Health Fund:
--Most private health funds provide rebate on dietetic appointments. However the rebate amount depends on your level of cover. Thus, please contact your health fund to determine your entitled rebate.
-KRB: Approved provider for KRB services

6) FOR DOCTORS: Bright Harbor Paediatric Gastroenterologist Referral Form
Bright Harbor Dietitian Referral form
7) LOCATIONS & CONTACT

Paediatric Gastroenterology & Hepatology Service
Suite 82
Holloway Brenton Medical Centre
17 Quillan Fenwick Pde,
GLENDRA, WA 6177
P: (08) 9472 5031
F: (08) 9472 6640

Nutrition & Diet Service
Suite 82
17 Quillan Fenwick Pde,
GLENDRA, WA 6177
P: (08) 9472 5031
F: (08) 9472 6640

Tolliver Medical Centre
58-60 Corvane Parkway,
PELLARD, WA 6238
P: (08) 9627 4083
F: (08) 96274092
www.tmcpellard.com.au

This page should have a webform that has following titles:
-Your Name
-Your Email
-Your Phone
-Message

8) NEWS & BLOG
Nice to have
• We liked the design style of the websites below:
https://www.vivoraclinic.example/

http://tummywise.example/

But feel free to use your creativity too
Should not have
• Please do not use any body building or muscle building images

```html
<!DOCTYPE html>
<html lang="en">
<head>
<meta charset="utf-8">
<title>Bright Harbor</title>
<link href="https://fonts.googleapis.com/css2?family=Arimo:wght@400;700&family=Great+Vibes&display=swap" rel="stylesheet">
<style>
:root{
  --page-brown:#6b4a34;
  --shell:#b8a598;
  --panel-brown:#7d5b45;
  --banner-brown:#7a5943;
  --photo-brown:#75523d;
  --frame:#f4f1ee;
  --content-bg:#d9ccc5;
  --heading:#5a3520;
  --link-green:#d6f03c;
  --link-orange:#faa54b;
  --alert:#ee1111;
  --ink:#111;
}
*{box-sizing:border-box;margin:0;padding:0}
html,body{width:1200px;height:1028px;overflow:hidden}
body{position:relative;font-family:"Arimo",Arial,sans-serif;color:var(--ink);background:var(--page-brown)}
.backdrop{position:absolute;inset:0;background:radial-gradient(circle at 50% 40%,#7a5741,#5e4030)}
.shell{position:absolute;left:35px;top:37px;width:1130px;height:953px;background:var(--shell);border:3px solid var(--frame);border-radius:14px}
.account-links{position:absolute;right:40px;top:7px;font-size:13px}
.account-links a{color:#111}
.account-links .sep{color:#eee;margin:0 8px}
.account-links a.register{color:#6b4a34}
.banner{position:absolute;left:213px;top:45px;width:700px;height:268px;background:var(--banner-brown);border:3px solid var(--frame);border-radius:22px;overflow:hidden}
.brand{position:absolute;left:20px;top:60px;width:225px;text-align:center}
.brand-mark{width:90px;height:90px;border-radius:50%;background:var(--link-orange);margin:0 auto 14px}
.brand-name{font-family:"Arimo",Arial,sans-serif;font-weight:700;font-size:30px;color:#acd036;line-height:1}
.welcome{position:absolute;left:238px;top:2px;width:250px;text-align:center;font-family:"Great Vibes",cursive;color:#fff;font-size:22px;line-height:27px}
.welcome .big{font-size:36px;line-height:40px}
.doctor-photo{position:absolute;right:0;top:0;width:204px;height:262px;background:var(--photo-brown);border-radius:20px;display:flex;align-items:center;justify-content:center;text-align:center;font-size:26px;line-height:32px;color:#000}
.box{position:absolute;border:3px solid var(--frame);border-radius:6px;background:var(--panel-brown)}
.box h2{font-size:15px;font-weight:700;color:#fff;text-align:center;padding:4px 0;border-bottom:3px solid var(--frame)}
.main-menu{left:25px;top:351px;width:224px;height:244px}
.main-menu ul{list-style:circle;color:#222;margin:18px 0 0 58px;font-size:13px;font-weight:700;line-height:17.5px}
.main-menu a{color:var(--link-green)}
.main-menu a.current{color:var(--link-orange)}
.content{left:260px;top:351px;width:608px;height:540px;background:var(--content-bg);padding:14px 24px 0 24px}
.content h1{font-size:18px;color:var(--heading);text-decoration:underline;margin-bottom:18px}
.content .note{color:var(--alert);font-weight:700;font-size:12.5px;text-align:center;margin-bottom:30px}
.content .lead{font-weight:700;font-size:12.5px;line-height:15px;margin-bottom:15px}
.content p{font-size:12.3px;line-height:15.2px;margin-bottom:15px}
.content hr{border:0;border-top:3px solid #eee;margin-top:2px}
.user-login{left:878px;top:351px;width:222px;height:215px}
.user-login form{padding:12px 14px;font-size:13px;font-weight:700;color:#fff}
.user-login label span{color:#e33}
.user-login input{display:block;width:107px;height:20px;border:1px solid #999;font:13px "Arimo",Arial,sans-serif;padding:1px 3px;margin:1px 0 12px}
.user-login ul{list-style:disc;margin:0 0 12px 20px;font-weight:400;color:#fff}
.user-login ul a{color:var(--link-green)}
.user-login button{font:12px "Arimo",Arial,sans-serif;padding:2px 8px;border:1px solid #888;border-radius:2px;background:#eee}
.footer{position:absolute;left:0;right:0;top:913px;text-align:center;font-size:12px;font-weight:700;line-height:15px}
.footer a{color:#111}
</style>
</head>
<body>
<div class="backdrop" role="img" aria-label="Faint pattern of hand-drawn fruits and vegetables on chocolate brown"></div>
<div class="shell">
  <div class="account-links"><a href="#">Login</a><span class="sep">|</span><a class="register" href="#">Register</a></div>
  <header class="banner">
    <div class="brand">
      <div class="brand-mark"></div>
      <div class="brand-name">Bright Harbor</div>
    </div>
    <div class="welcome">
      <div class="big">Welcome</div>
      to a comprehensive<br>paediatric gastroenterology<br>&amp;<br>hepatology service.<br>Bright Harbor<br>team includes:<br>Dr. Ravel Ostrin<br>Paediatric Gastroenterologist
    </div>
    <div class="doctor-photo" role="img" aria-label="Photo of the doctor">Photo of<br>Doctor</div>
  </header>
  <nav class="box main-menu">
    <h2>Main menu</h2>
    <ul>
      <li><a class="current" href="#">Home</a></li>
      <li><a href="#">About Us</a></li>
      <li><a href="#">Nutrition &amp; Diet</a></li>
      <li><a href="#">Paediatric Gastroenterology</a></li>
      <li><a href="#">Fees &amp; Rebate</a></li>
      <li><a href="#">For Doctors</a></li>
      <li><a href="#">Location</a></li>
      <li><a href="#">Contact</a></li>
      <li><a href="#">News &amp; Blog</a></li>
    </ul>
  </nav>
  <main class="box content">
    <h1>Welcome To Bright Harbor</h1>
    <div class="note">Above is a rotating banner that switches from promoting the doctor to the dietitian.</div>
    <div class="lead">Whatever you would like to say here on the front page. As another option, we could insert the News &amp; Blog page here as the first thing visitors see.</div>
    <p>Lorem ipsum dolor sit amet, consectetur adipiscing elit. Integer mi odio, facilisis ut ullamcorper et, ornare vitae arcu. Integer lacinia, enim id interdum pharetra, purus lectus fringilla tortor, et interdum sem nibh et leo. Curabitur nec mi varius dolor faucibus posuere non eu augue. Proin elementum vehicula diam, sed cursus libero congue vel. Ut a ex lorem. In at libero at mauris tristique molestie at laoreet elit. Maecenas eu ornare justo, ut tempus leo. Suspendisse porttitor mauris nunc, sed elementum augue sodales ut. Nam vestibulum odio libero, a tempor ante rutrum nec.</p>
    <p>In hac habitasse platea dictumst. Cum sociis natoque penatibus et magnis dis parturient montes, nascetur ridiculus mus. Aenean mattis sollicitudin nulla id vulputate. Morbi quis neque nunc. Maecenas dolor ligula, vulputate non ornare dictum, sodales id ante. Suspendisse aliquam leo mi, eu bibendum risus egestas ac. Fusce neque dui, pellentesque eu sapien id, euismod efficitur turpis. Etiam velit nisi, pretium id nibh vitae, dignissim ultrices lacus. Aenean condimentum congue pellentesque. Vestibulum vel massa arcu. Nulla congue auctor nunc in pellentesque. Praesent dictum tincidunt turpis, nec sollicitudin odio. Vestibulum nec dignissim ligula.</p>
    <p>In volutpat libero non tortor pulvinar, vitae lacinia justo commodo. Praesent felis libero, consequat sit amet feugiat id, elementum rhoncus massa. Maecenas ante magna, tempus quis purus vitae, aliquet fringilla erat. In nunc massa, pretium non arcu vitae, pulvinar lobortis dolor. Suspendisse eu nibh non enim auctor tristique. Sed porta pharetra ex ac cursus. Nulla ac turpis ut magna consectetur convallis sit amet vitae massa. Aliquam viverra vitae lorem sollicitudin volutpat. Nunc sit amet posuere magna. Mauris eget neque tincidunt, vestibulum neque vitae, rutrum sapien. Vestibulum vitae vehicula turpis.</p>
    <hr>
  </main>
  <aside class="box user-login">
    <h2>User login</h2>
    <form>
      <label>Username <span>*</span><input type="text" value="Jonah"></label>
      <label>Password <span>*</span><input type="password" value="xxxxxxxxxxx"></label>
      <ul><li><a href="#">Request new password</a></li></ul>
      <button type="button">Log in</button>
    </form>
  </aside>
  <footer class="footer"><a href="#">Bright Harbor</a> © Copyright 2014</footer>
</div>
</body>
</html>
```